External Window Signage Design - Dentist

We have 5 windows that need to have new signage designed for a Dental Clinic based in a community shopping centre.
The windows mostly line up but there is one smaller window which is lower to the ground. All 5 windows are to be covered with vinyl graphics
The windows all face the shopping centre car park under an awning.

We have attached the measurements of the window to have graphics.
We will be placing perforated once way vision vinyl as a material on the external glass. We have also attach our logo design.

We would like something simple and creative for our design. Stock images should only be used to aid in aethetics but not form the basis of the design. We prefer simple custom graphics that identifies us as a clean, modern dental clinic. We are marketing ourselves as a modern fully digital clinic where all examinations are done on a big screen which photography and 3d scanners.

Please include the words below.

Marlow Ridge Dental

Children's Dentistry
Digital Dentistry
Cosmetic Dentistry
Clearvanta
Family Dental Care
Where quality meets value - This one is our slogan, and not a service. Please use it as such.
Same Day Emergency Bookings

Please include in small text our website and phone number.
www.marlowridgedental.com.au
Phone Number TBD: 87650432

Open to different colors but our main theme is blues and greens. Similar to our logo.

Target Market(s)

20 - 40 year old dental patients. Middle Class. Some retirees as well.

Industry/Entity Type

Dental Clinic

Font styles to use
Other font styles liked:
• Comfortaa

Colors
33b8a4
34a6d7

Requirements
Must have
• Simple elegant graphics. Stock photos to aid in design if needed.
Nice to have
• Simple designs with greys, greens and blues. As per our logo.
Comfortaa font
Should not have
• Overbearing stock imagery.
Too many colors.

```html
<!DOCTYPE html>
<html lang="en">
<head>
<meta charset="utf-8">
<title>Marlow Ridge Dental – Window Signage</title>
<link href="https://fonts.googleapis.com/css2?family=Comfortaa:wght@400;700&family=Poppins:wght@400;500&display=swap" rel="stylesheet">
<style>
  :root {
    --backdrop: #4a4a4a;
    --panel: #ffffff;
    --blue: #1a90d8;
    --green: #7cc243;
    --teal: #33b8a4;
    --teal-deep: #2fa58d;
    --grey-text: #6b6d70;
    --ink: #3a3a3a;
  }
  * { margin: 0; padding: 0; box-sizing: border-box; }
  html, body { width: 1154px; height: 1200px; overflow: hidden; }
  body { background: var(--backdrop); position: relative; font-family: "Poppins", sans-serif; }

  .window-panel {
    position: absolute; top: 378px; height: 443px;
    background: var(--panel); overflow: hidden;
  }
  .panel-narrow { left: 30px;  width: 120px; }
  .panel-phone  { left: 174px; width: 237px; }
  .panel-services { left: 421px; width: 237px; }
  .panel-web    { left: 668px; width: 238px; }
  .panel-end    { left: 922px; width: 204px; }

  .wave { position: absolute; left: 0; width: 100%; display: block; }
  .wave-top { top: 0; height: 52px; }
  .wave-bottom { bottom: 0; height: 78px; }
  .fill-blue { fill: var(--blue); }
  .fill-green { fill: var(--green); }
  .line-blue { fill: none; stroke: var(--blue); stroke-width: 3; }
  .line-green { fill: none; stroke: var(--green); stroke-width: 4; }

  .brand {
    position: absolute; left: 0; width: 100%;
    display: flex; flex-direction: column; align-items: center;
  }
  .brand-dot { width: 48px; height: 48px; border-radius: 50%; background: var(--blue); margin-bottom: 12px; }
  .brand-name {
    font-family: "Comfortaa", sans-serif; font-weight: 400;
    color: var(--grey-text); font-size: 18px; white-space: nowrap;
  }
  .brand-small .brand-dot { width: 26px; height: 26px; margin-bottom: 7px; }
  .brand-small .brand-name { font-size: 10px; }
  .panel-narrow .brand { top: 135px; }
  .panel-phone .brand, .panel-web .brand, .panel-end .brand { top: 135px; }
  .panel-services .brand { top: 70px; }

  .contact-pill {
    position: absolute; top: 270px; left: 50%; transform: translateX(-50%);
    height: 18px; padding: 0 10px; background: var(--teal-deep); color: #fff;
    font-size: 8px; display: flex; align-items: center; gap: 5px; white-space: nowrap; border-radius: 1px;
  }
  .contact-pill svg { width: 9px; height: 9px; fill: #fff; }
  .panel-phone .contact-pill { width: 158px; justify-content: center; }

  .services-title {
    position: absolute; top: 168px; left: 12px; width: 212px; height: 24px;
    background: var(--teal); color: #fff; font-size: 13px; font-weight: 500;
    display: flex; align-items: center; justify-content: center; white-space: nowrap;
  }
  .service-list { position: absolute; top: 199px; left: 20px; list-style: none; }
  .service-list li {
    font-size: 11.5px; color: var(--ink); height: 23px; line-height: 23px;
    display: flex; align-items: center; gap: 10px; white-space: nowrap;
  }
  .service-list li::before {
    content: ""; width: 5px; height: 5px; background: var(--teal); transform: rotate(45deg);
  }
</style>
</head>
<body>

<svg width="0" height="0" style="position:absolute">
  <defs>
    <g id="wave-top-art">
      <path class="fill-blue" d="M0 0 H240 V4 C170 6 90 16 0 14 Z"/>
      <path class="line-green" d="M0 22 C70 26 150 8 240 16"/>
      <path class="line-blue" d="M0 32 C80 36 160 22 240 26"/>
    </g>
    <g id="wave-bottom-art">
      <path class="fill-green" d="M0 6 C70 22 160 34 240 30 V38 C160 44 70 36 0 20 Z"/>
      <path class="line-green" d="M0 34 C80 46 160 48 240 44"/>
      <path class="fill-blue" d="M0 48 C80 60 170 62 240 56 V80 H0 Z"/>
    </g>
  </defs>
</svg>

<section class="window-panel panel-narrow">
  <svg class="wave wave-top" viewBox="0 0 240 52" preserveAspectRatio="none"><use href="#wave-top-art"/></svg>
  <div class="brand brand-small"><span class="brand-dot"></span><span class="brand-name">Marlow Ridge Dental</span></div>
  <svg class="wave wave-bottom" viewBox="0 0 240 80" preserveAspectRatio="none"><use href="#wave-bottom-art"/></svg>
</section>

<section class="window-panel panel-phone">
  <svg class="wave wave-top" viewBox="0 0 240 52" preserveAspectRatio="none"><use href="#wave-top-art"/></svg>
  <div class="brand"><span class="brand-dot"></span><span class="brand-name">Marlow Ridge Dental</span></div>
  <div class="contact-pill">
    <svg viewBox="0 0 24 24"><path d="M6.6 10.8a15.1 15.1 0 0 0 6.6 6.6l2.2-2.2a1 1 0 0 1 1-.25 11.4 11.4 0 0 0 3.6.57 1 1 0 0 1 1 1V20a1 1 0 0 1-1 1A17 17 0 0 1 3 4a1 1 0 0 1 1-1h3.5a1 1 0 0 1 1 1c0 1.25.2 2.45.57 3.57a1 1 0 0 1-.25 1z"/></svg>
    TBD : 87650432
  </div>
  <svg class="wave wave-bottom" viewBox="0 0 240 80" preserveAspectRatio="none"><use href="#wave-bottom-art"/></svg>
</section>

<section class="window-panel panel-services">
  <svg class="wave wave-top" viewBox="0 0 240 52" preserveAspectRatio="none"><use href="#wave-top-art"/></svg>
  <div class="brand"><span class="brand-dot"></span><span class="brand-name">Marlow Ridge Dental</span></div>
  <h1 class="services-title">MARLOW RIDGE DENTAL</h1>
  <ul class="service-list">
    <li>Children's Dentistry</li>
    <li>Digital Dentistry</li>
    <li>Cosmetic Dentistry</li>
    <li>Clearvanta</li>
    <li>Family Dental Care</li>
    <li>Where quality meets value</li>
    <li>Same Day Emergency Bookings</li>
  </ul>
  <svg class="wave wave-bottom" viewBox="0 0 240 80" preserveAspectRatio="none"><use href="#wave-bottom-art"/></svg>
</section>

<section class="window-panel panel-web">
  <svg class="wave wave-top" viewBox="0 0 240 52" preserveAspectRatio="none"><use href="#wave-top-art"/></svg>
  <div class="brand"><span class="brand-dot"></span><span class="brand-name">Marlow Ridge Dental</span></div>
  <div class="contact-pill">www.marlowridgedental.com.au</div>
  <svg class="wave wave-bottom" viewBox="0 0 240 80" preserveAspectRatio="none"><use href="#wave-bottom-art"/></svg>
</section>

<section class="window-panel panel-end">
  <svg class="wave wave-top" viewBox="0 0 240 52" preserveAspectRatio="none"><use href="#wave-top-art"/></svg>
  <div class="brand"><span class="brand-dot"></span><span class="brand-name">Marlow Ridge Dental</span></div>
  <svg class="wave wave-bottom" viewBox="0 0 240 80" preserveAspectRatio="none"><use href="#wave-bottom-art"/></svg>
</section>

</body>
</html>
```